Teachers workshop flyer

I need a flyer to inform schools of a workshop for teachers that empowers the teacher to help traumatised and disadvantaged students to engage in successful learning.

I am a teacher and educator and my info for the flyer is attached.

Target Market(s)

Principals and vice-principals who have stressed staff and students and they want things to be better in the school!

Industry/Entity Type

Teacher

```html
<!DOCTYPE html>
<html lang="en">
<head>
<meta charset="utf-8">
<title>Brain-based Strategies for Student Success</title>
<link rel="stylesheet" href="https://fonts.googleapis.com/css2?family=Oswald:wght@600&family=Roboto+Condensed:wght@700&display=swap">
<style>
  :root {
    --ink: #000000;
    --paper: #ffffff;
    --title-red: #e8202a;
    --presenter-yellow: #ffe81a;
    --cta-blue: #1f9bd7;
    --scene-dark: #000000;
    --scene-warm: #2e2417;
  }
  * { margin: 0; padding: 0; box-sizing: border-box; }
  html, body { width: 933px; height: 1200px; overflow: hidden; background: var(--ink); }
  .flyer {
    position: relative;
    width: 933px;
    height: 1200px;
    background: var(--ink);
    color: var(--paper);
    font-family: "Roboto Condensed", "Arial Narrow", sans-serif;
    font-weight: 700;
    overflow: hidden;
  }
  .line { display: block; white-space: nowrap; }
  .title-band {
    position: absolute;
    left: 0; top: 22px;
    width: 933px; height: 58px;
    background: var(--paper);
    text-align: center;
  }
  .title {
    font-family: "Oswald", "Arial Narrow", sans-serif;
    font-weight: 600;
    font-size: 44px;
    line-height: 58px;
    color: var(--title-red);
    letter-spacing: 3.4px;
    white-space: nowrap;
  }
  .intro {
    position: absolute;
    left: 58px; top: 100px;
    width: 840px;
    font-size: 16.5px;
    line-height: 22.5px;
    letter-spacing: 2px;
  }
  .intro p + p { margin-top: 17px; }
  .rule {
    position: absolute;
    left: 173px;
    width: 590px;
    height: 5px;
    background: var(--paper);
  }
  .rule-top { top: 324px; }
  .rule-mid { top: 512px; }
  .rule-short { left: 374px; width: 216px; height: 2px; top: 610px; }
  .section-heading {
    position: absolute;
    left: 0; width: 933px;
    text-align: center;
    font-size: 18.5px;
    letter-spacing: 1.6px;
  }
  .presenter-heading { top: 338px; color: var(--presenter-yellow); }
  .presenter-bio {
    position: absolute;
    left: 0; top: 374px;
    width: 933px;
    text-align: center;
    font-size: 14.3px;
    line-height: 21px;
    letter-spacing: 1.7px;
    color: var(--presenter-yellow);
  }
  .feedback-heading { top: 526px; font-size: 19px; }
  .testimonial {
    position: absolute;
    left: 0; top: 561px;
    width: 933px;
    text-align: center;
    font-size: 14.3px;
    line-height: 22px;
    letter-spacing: 1.5px;
  }
  .lightbulb-heading { top: 625px; font-size: 19px; }
  .lightbulb-list {
    position: absolute;
    left: 0; top: 657px;
    width: 933px;
    list-style: none;
    text-align: center;
    font-size: 14.3px;
    line-height: 21.5px;
    letter-spacing: 1.5px;
  }
  .call-to-action {
    position: absolute;
    left: 0; top: 732px;
    width: 933px;
    text-align: center;
    color: var(--cta-blue);
    font-size: 28px;
    line-height: 40px;
    letter-spacing: 2.6px;
  }
  .hero-image {
    position: absolute;
    left: 0; top: 812px;
    width: 933px; height: 388px;
    background: linear-gradient(180deg, var(--scene-dark) 0%, var(--scene-warm) 100%);
  }
</style>
</head>
<body>
<main class="flyer">
  <header class="title-band">
    <h1 class="title">Brain-based Strategies for Student Success</h1>
  </header>

  <section class="intro">
    <p>
      <span class="line">Contemporary teaching is a highly complex role as increasing numbers of students</span>
      <span class="line">attend school without the essential ‘self-skills’ to be truly ‘school-ready’ and successful.</span>
      <span class="line">Instead these students often seek-out attention in ways that can disruptive in the</span>
      <span class="line">classroom causing stress and frustration for teachers.</span>
    </p>
    <p>
      <span class="line">Dan shows how and why the most effective strategies for these students are guided by</span>
      <span class="line">a sound understanding of child-development and brain-development - especially where</span>
      <span class="line">trauma has left lasting impacts. Teachers can learn how tobuild a student’s self-skills,</span>
      <span class="line">without the teacher having to become a therapist!</span>
    </p>
  </section>

  <div class="rule rule-top"></div>
  <h2 class="section-heading presenter-heading">About the Presenter:</h2>
  <p class="presenter-bio">
    <span class="line">Daniel Whitmore is a Melbourne-based therapist and educator with</span>
    <span class="line">over twenty years experience working with adults and young people</span>
    <span class="line">in the area of trauma and recovery. Dan’s seminars are engaging and</span>
    <span class="line">practical since teachers need effective strategies that will immediately</span>
    <span class="line">translate into classroom practice. Dan has trained here and overseas</span>
    <span class="line">in the most effective behavior change strategies.</span>
  </p>
  <div class="rule rule-mid"></div>

  <h2 class="section-heading feedback-heading">Teacher Feedback:</h2>
  <blockquote class="testimonial">
    <span class="line">“Dan was such an engaging and energetic presenter whom I enjoyed immensely. His presentation on the</span>
    <span class="line">brain and take away strategies were so practical and meaningful. It was an invaluable session.”</span>
  </blockquote>
  <div class="rule rule-short"></div>

  <h2 class="section-heading lightbulb-heading">“My Light-bulb moments:</h2>
  <ul class="lightbulb-list">
    <li>- I need to CONNECT – not correct – far more often.</li>
    <li>- Seeing negative self-talk for what it is.</li>
    <li>- Using far more ‘diversions’ in the avoidance loop.”</li>
  </ul>

  <p class="call-to-action">
    <span class="line">Call 0400 512 390 for more information or to book Dan to come</span>
    <span class="line">to your school:www.danielwhitmore.com.au/studentsuccess</span>
  </p>

  <div class="hero-image" role="img" aria-label="Photograph of a red apple floating above an open book whose pages show a heart-shaped shadow"></div>
</main>
</body>
</html>
```